Swimming Pool Supply Company Business Cards

We need business cards designed for company. These need to be easy to edit so that we can fill in names, titles, and contact info for each person who works here.

Dalton R. Whitfield
Manager of Legal & Finance
K.L. Brisbane, Incorporated

4837 Grenway Avenue
Marlow Heights, PA 19243

E. dalton@klbrisbane-example.com
M. (215) 555-0173
O. (215) 555-0148

Contact Information for Business Card

Looking to upgrade current business cards with graphic that can be edited. Looking for fresh ideas for an age old industry.

Font styles to use
Serif
Sans Serif

Colors

Designer to choose colors to be used in the design.

Requirements
Must have
• Professional, fresh, unique but professional

```html
<!DOCTYPE html>
<html lang="en">
<head>
<meta charset="utf-8">
<title>K.L. Brisbane Business Card</title>
<link href="https://fonts.googleapis.com/css2?family=Source+Sans+3:wght@400;600&display=swap" rel="stylesheet">
<style>
  :root {
    --page: #ffffff;
    --frame: #8a8a8a;
    --card-deep: #2d3190;
    --card-light: #373b9a;
    --tagline: #9c9ec6;
    --wordmark: #b6b8dc;
    --contact: #a9abf0;
  }
  * { margin: 0; padding: 0; box-sizing: border-box; }
  html, body {
    width: 1200px; height: 1200px; overflow: hidden;
    background: var(--page);
    font-family: "Source Sans 3", sans-serif;
  }
  .sheet { position: relative; width: 1200px; height: 1200px; }
  .trim {
    position: absolute; left: 220px; width: 761px; height: 478px;
    border: 1px solid var(--frame);
  }
  .trim--front { top: 98px; }
  .trim--back { top: 624px; }
  .card {
    position: absolute; left: 16px; top: 16px; width: 727px; height: 445px;
    border-radius: 10px; overflow: hidden;
  }
  .card__water {
    position: absolute; inset: 0; width: 100%; height: 100%;
  }
  .line {
    position: absolute; white-space: nowrap; line-height: 1;
    color: var(--contact); font-size: 18px;
  }
  .centered { transform: translateX(-50%); }
  .tagline {
    left: 363px; top: 13px; font-size: 29px; color: var(--tagline); font-weight: 400;
  }
  .wordmark {
    color: var(--wordmark); font-weight: 600; letter-spacing: 4px;
  }
  .wordmark--front { left: 363px; top: 70px; font-size: 88px; }
  .wordmark--back { left: 363px; top: 150px; font-size: 104px; }
  .identity { left: 380px; text-align: center; }
  .address { left: 256px; text-align: center; }
  .phones { left: 441px; }
  .web { left: 363px; }
</style>
</head>
<body>
<main class="sheet">

  <section class="trim trim--front">
    <div class="card">
      <svg class="card__water" role="img" aria-label="Rippling pool water pattern" viewBox="0 0 727 445" preserveAspectRatio="none">
        <defs>
          <linearGradient id="water-front" x1="0" y1="0" x2="0" y2="1">
            <stop offset="0" stop-color="#33379a"/>
            <stop offset="0.5" stop-color="#2f3393"/>
            <stop offset="1" stop-color="#33379a"/>
          </linearGradient>
        </defs>
        <rect width="727" height="445" fill="url(#water-front)"/>
      </svg>
      <p class="line centered tagline">Big Enough to Serve You, Small Enough to Care</p>
      <p class="line centered wordmark wordmark--front">BRISBANE</p>

      <p class="line centered identity" style="top:221px">Dalton R. Whitfield</p>
      <p class="line centered identity" style="top:245px">Manager of Legal &amp; Finance</p>
      <p class="line centered identity" style="top:268px">K.L. Brisbane, Incorporated</p>

      <p class="line centered address" style="top:305px">4837 Grenway Avenue</p>
      <p class="line centered address" style="top:329px">Marlow Heights, PA 19243</p>

      <p class="line phones" style="top:305px">M. (215) 555-0173</p>
      <p class="line phones" style="top:329px">O. (215) 555-0148</p>

      <p class="line centered identity" style="top:361px">E. dalton@klbrisbane-example.com</p>
      <p class="line centered web" style="top:402px">www.klbrisbane-example.com</p>
    </div>
  </section>

  <section class="trim trim--back">
    <div class="card">
      <svg class="card__water" role="img" aria-label="Rippling pool water pattern" viewBox="0 0 727 445" preserveAspectRatio="none">
        <defs>
          <linearGradient id="water-back" x1="0" y1="0" x2="0" y2="1">
            <stop offset="0" stop-color="#33379a"/>
            <stop offset="0.5" stop-color="#2f3393"/>
            <stop offset="1" stop-color="#33379a"/>
          </linearGradient>
        </defs>
        <rect width="727" height="445" fill="url(#water-back)"/>
      </svg>
      <p class="line centered wordmark wordmark--back">BRISBANE</p>
      <p class="line centered web" style="top:409px">www.klbrisbane-example.com</p>
    </div>
  </section>

</main>
</body>
</html>
```